label redesign for skincare product

We would like a redesign of existing labels for a skincare product that we make (the existing labels are attached). This is a very natural product, but the existing labels are not right - one of the labels wraps around the jar, and one of the labels is placed on the bottom of the jar (copies of these attached). It needs softening and to be made less brutal looking. The label needs to communicate luxury quality product, that contains natural products, whilst maintaining a contemporary feel. The audience is male and female.

The product is called 'Dew Haven' and our company is called BR Naturals. We have a website at www.brnaturals-example.com where the existing product can be seen. It is NOT however necessary for the BR Naturals logo from the website to be used on the label - this is at the discretion of the designer.

The packaging will remain the same - this is a glass jar in extremely deep purple, almost black.

The colour of the product inside the jar is off white. The product contain mandarin and geranium essential oils so is floral and citrussy smelling.

Target Market(s)

Adults who like high quality natural skincare products, 30-65.

Industry/Entity Type

It Company

Font styles to use
Serif
Sans Serif

Colors

Designer to choose colors to be used in the design.

Requirements
Must have
• The long label must by 13mm high and 110 mm wide. The round label for the back of the jar must be 40mm diameter..

```html
<!DOCTYPE html>
<html lang="en">
<head>
<meta charset="utf-8">
<title>Dew Haven – Label Set</title>
<link rel="stylesheet" href="https://fonts.googleapis.com/css2?family=Josefin+Sans:wght@100;200;300&family=Arimo:wght@400;700&display=swap">
<style>
  :root {
    --label-lime: #c5d227;
    --label-ink: #ffffff;
    --backdrop-top: #ffffff;
    --backdrop-bottom: #e9e9e9;
  }
  * { box-sizing: border-box; margin: 0; padding: 0; }
  html, body { width: 1200px; height: 1200px; overflow: hidden; }
  body {
    position: relative;
    background: radial-gradient(ellipse at 50% 45%, var(--backdrop-top) 0%, var(--backdrop-bottom) 100%);
    font-family: "Arimo", Arial, sans-serif;
    color: var(--label-ink);
  }

  /* Brand lockup shared by the front labels */
  .brand-lockup { text-align: center; }
  .brand-lockup .company {
    font-family: "Josefin Sans", sans-serif;
    font-weight: 300;
    letter-spacing: 0.04em;
    white-space: nowrap;
  }
  .brand-lockup .product {
    font-family: "Josefin Sans", sans-serif;
    font-weight: 100;
    line-height: 1;
    letter-spacing: 0.05em;
    white-space: nowrap;
  }
  .brand-lockup .rule {
    position: relative;
    border-top: 1px solid var(--label-ink);
    margin: 0 auto;
  }
  .brand-lockup .rule::after {
    content: "";
    position: absolute;
    left: 50%;
    top: -1px;
    transform: translate(-50%, -50%);
    border: 1px solid var(--label-ink);
    border-radius: 50%;
    background: var(--label-lime);
  }

  /* Top front label */
  .front-label {
    position: absolute;
    left: 130px; top: 0;
    width: 418px; height: 172px;
    background: var(--label-lime);
    padding-top: 52px;
  }
  .front-label .company { font-size: 16px; }
  .front-label .product { font-size: 54px; margin-top: 6px; }
  .front-label .rule { width: 360px; margin-top: 8px; }
  .front-label .rule::after { width: 12px; height: 12px; }

  /* Round back labels */
  .round-label {
    position: absolute;
    border-radius: 50%;
    background: var(--label-lime);
    text-align: center;
    display: flex;
    flex-direction: column;
    align-items: center;
    justify-content: center;
  }
  .round-label .title { font-weight: 700; }
  .round-label .heading { margin-top: 0.7em; }
  .round-label .active { margin-top: 0.8em; }
  .round-label .contact { margin-top: 0.8em; }
  .round-label .web { font-weight: 700; }

  .round-label--large {
    left: 560px; top: 240px;
    width: 580px; height: 580px;
    font-size: 16.5px;
    line-height: 1.3;
    padding: 0 50px;
  }
  .round-label--large .mark-rule {
    width: 200px; border-top: 1px solid var(--label-ink);
    position: relative; margin-bottom: 20px;
  }
  .round-label--large .mark-rule::after {
    content: ""; position: absolute; left: 50%; top: -1px;
    width: 14px; height: 14px; transform: translate(-50%, -50%);
    border: 1px solid var(--label-ink); border-radius: 50%;
    background: var(--label-lime);
  }

  .round-label--small {
    left: 42px; top: 930px;
    width: 240px; height: 240px;
    font-size: 7.4px;
    line-height: 1.28;
    padding: 0 14px;
  }

  /* Long wrap label */
  .wrap-label {
    position: absolute;
    left: 310px; top: 1086px;
    width: 876px; height: 102px;
    background: var(--label-lime);
    display: flex;
    align-items: center;
    padding-left: 20px;
  }
  .wrap-label .brand-lockup { width: 280px; flex: none; }
  .wrap-label .company { font-size: 12px; }
  .wrap-label .product { font-size: 38px; margin-top: 4px; }
  .wrap-label .rule { width: 250px; margin-top: 6px; }
  .wrap-label .rule::after { width: 9px; height: 9px; }
  .wrap-label .details {
    width: 380px;
    margin-left: 34px;
    font-size: 7.6px;
    line-height: 1.32;
  }
  .wrap-label .details .title { font-weight: 700; font-size: 8px; margin-bottom: 3px; }
  .wrap-label .details .web { font-weight: 700; }
</style>
</head>
<body>

  <section class="front-label brand-lockup">
    <div class="company">BR NATURALS</div>
    <div class="product">DEW HAVEN</div>
    <div class="rule"></div>
  </section>

  <section class="round-label round-label--large">
    <div class="mark-rule"></div>
    <div class="title">BR Naturals Dew Haven</div>
    <div>Moisturing body salve for dry skin</div>
    <div class="heading">Ingredients:</div>
    <div>Helianthus Annuus (Sunflower) Oil,<br>Prunus Dulcis (Sweet Almond) Oil,<br>Cera Alba (beeswax), Vitis Vinifera (Grapeseed) Oil,<br>Calendula Sylvestre (Calendula) Extract,<br>Citrus Reticulata (Green Mandarin) Oil*,<br>Pelargonium Graveolens Roseum (Geranium) Oil*,<br>Benzyl Alcohol, Salicylic Acid, Glycerine,<br>Sorbic Acid.</div>
    <div class="active">Active ingredients: Cinnamal, Citronellol,<br>Geraniol, Limonene, Linalool.</div>
    <div class="contact">* Organic Ingredients<br>support@brnaturals-example.com</div>
    <div class="web">www.brnaturals-example.com</div>
    <div>100ml &#8494; 3.2fl.oz.</div>
  </section>

  <section class="round-label round-label--small">
    <div class="title">BR Naturals Dew Haven</div>
    <div>Moisturing body salve for dry skin</div>
    <div class="heading">Ingredients:</div>
    <div>Helianthus Annuus (Sunflower) Oil,<br>Prunus Dulcis (Sweet Almond) Oil,<br>Cera Alba (beeswax), Vitis Vinifera (Grapeseed) Oil,<br>Calendula Sylvestre (Calendula) Extract,<br>Citrus Reticulata (Green Mandarin) Oil*,<br>Pelargonium Graveolens Roseum (Geranium) Oil*,<br>Benzyl Alcohol, Salicylic Acid, Glycerine,<br>Sorbic Acid.</div>
    <div class="active">Active ingredients: Cinnamal, Citronellol,<br>Geraniol, Limonene, Linalool.</div>
    <div class="contact">* Organic Ingredients<br>support@brnaturals-example.com</div>
    <div class="web">www.brnaturals-example.com</div>
    <div>100ml &#8494; 3.2fl.oz.</div>
  </section>

  <section class="wrap-label">
    <div class="brand-lockup">
      <div class="company">BR NATURALS</div>
      <div class="product">DEW HAVEN</div>
      <div class="rule"></div>
    </div>
    <div class="details">
      <div class="title">BR Naturals Dew Haven with Calendula, Green Mandarin and Geranium.</div>
      <div>Moisturing salve body for dry skin with naturally occuring active ingredients. Apply to dry skin that needs some love. Keep out of the reach of children. For external use only. Test on a small patch of skin before general application. Whilst unlikely, if you experience skin irritation stop using this product and consult a doctor. Store in a cool, dry place. No animal testing. BR Naturals, 8 Willow Row, London N4 7QT. <span class="web">www.brnaturals-example.com</span></div>
    </div>
  </section>

</body>
</html>
```